A online shop for solid wood need a Stationary design

A new online shop (in Austria and Germany) for solid wood and steel furniture (feldberg-formwerk) needs a Stationay design (letterhead, business card, envelope etc...). Dining tables, coffee tables, TV furniture and similar furniture will be sold. Everything will be custom made.

```html
<!DOCTYPE html>
<html lang="en">
<head>
<meta charset="utf-8">
<title>Feldberg Formwerk – Business Card</title>
<link rel="stylesheet" href="https://fonts.googleapis.com/css2?family=Lato:wght@400;700&family=Oswald:wght@500&display=swap">
<style>
  :root {
    --backdrop: #727272;
    --card-dark: #2c2a2b;
    --brand-red: #ed1c24;
    --text-light: #ffffff;
    --wordmark: #8a8a8a;
  }
  html, body {
    margin: 0;
    padding: 0;
    overflow: hidden;
  }
  .canvas {
    position: relative;
    width: 1200px;
    height: 1200px;
    background: var(--backdrop);
    overflow: hidden;
  }
  .card {
    position: absolute;
    left: 262px;
    width: 685px;
    height: 391px;
    border-radius: 26px;
    background: var(--card-dark);
    overflow: hidden;
  }
  .card--front { top: 165px; }
  .card--back  { top: 653px; }

  .accent-panel {
    position: absolute;
    left: 260px;
    top: 0;
    right: 0;
    bottom: 0;
    background: var(--brand-red);
    border-bottom-left-radius: 70px;
    display: flex;
    flex-direction: column;
    align-items: center;
    justify-content: center;
    gap: 26px;
  }
  .accent-panel__square {
    width: 96px;
    height: 96px;
    background: var(--text-light);
  }
  .accent-panel__name {
    margin: 0;
    text-align: center;
    font-family: "Lato", sans-serif;
    font-weight: 700;
    font-size: 34px;
    line-height: 42px;
    letter-spacing: 6px;
    color: var(--text-light);
    text-transform: uppercase;
  }

  .contact {
    position: absolute;
    left: 38px;
    top: 80px;
    color: var(--text-light);
    font-family: "Lato", sans-serif;
    font-size: 16px;
    line-height: 19.5px;
  }
  .contact__name {
    margin: 0;
    font-family: "Oswald", sans-serif;
    font-weight: 500;
    font-size: 27px;
    line-height: 32px;
    color: var(--brand-red);
    letter-spacing: 0.2px;
    text-transform: uppercase;
  }
  .contact__role { margin: 0 0 22px; }
  .contact__address { margin: 0 0 12px; font-style: normal; }
  .contact__lines { margin: 0; }

  .wordmark {
    position: absolute;
    left: 0;
    right: 0;
    top: 50%;
    transform: translateY(-50%);
    margin: 0;
    text-align: center;
    font-family: "Lato", sans-serif;
    font-weight: 700;
    font-size: 34px;
    letter-spacing: 6px;
    color: var(--wordmark);
    text-transform: uppercase;
  }
</style>
</head>
<body>
<main class="canvas">
  <section class="card card--front" aria-label="Business card front">
    <div class="contact">
      <h1 class="contact__name">Jonas Brenner</h1>
      <p class="contact__role">President</p>
      <address class="contact__address">14 Lindenweg<br>Salzburg, Austria 5020</address>
      <p class="contact__lines">
        P. 0662-418-207<br>
        C. 0664-732-915<br>
        info@feldbergformwerk.com<br>
        www.feldbergformwerk.com
      </p>
    </div>
    <div class="accent-panel">
      <div class="accent-panel__square"></div>
      <p class="accent-panel__name">Feldberg<br>Formwerk</p>
    </div>
  </section>

  <section class="card card--back" aria-label="Business card back">
    <p class="wordmark">Feldberg Formwerk</p>
  </section>
</main>
</body>
</html>
```